Design letter head and business card

Hello,

you should design a business card and letter paper for Sturmfalke Werbung. In German we write this word with K insteat of C.

Company does not have a logo. But in general, we write Sturmfalke Werbung in 2 lines.
First line red: STURMFALKE
Second line gray: WERBUNG

Red (or wine red) and Gray / Black are our favorite colors.

Company slogan: "Higher Ground Web Promotion".

Company offers SEO, SEM, SEA, AdWords, Conversion Optimization, Online Markting Consulting ...

The website is old, please do not use this as base for your task.

German letter paper sizes:
Viawable Dimensions : 210 x 297 mm
Needed file dimensions: 212 x 299 mm

Informations to include:

Address:
Sturmfalke Werbung GmbH
Lindenweg 23
72619 Rebenfeld
Germany

Geschäftsführer | CEO: Rüdiger Pfannholz

Phone: +49 (0) 7284 562 71 48

Fax: +49 (0) 7284 562 71 77

Mail: info@sturmfalke-werbung-beispiel.de

Web: www.sturmfalke-werbung-beispiel.de

Amtsgericht Suttgart, HRB 734562

Bank: Grauselder Kasse
IBAN: DE917253108400XXXXXXXX
BIC: RAVQDEM2GKX

Thanks

Rüdiger

Target Market(s)

People who likes to win the online marketing game.

Industry/Entity Type

Business

Contact Information for Business Card

Here is the personal text on the card:

Name:
Rüdiger Pfannholz

Title:
Geschäftsführer | CEO

Address:
Sturmfalke Werbung GmbH
Lindenweg 23
72619 Rebenfeld
Germany

Phone:
+49 (0) 7284 562 71 48

Fax:
+49 (0) 7284 562 71 77

Mail:
pfannholz@sturmfalke-werbung-beispiel.de

Web:
www.sturmfalke-werbung-beispiel.de

Business Card:
Viewable Dimensions: 85 x 55 mm
Needed file dimensions: 87 x 57mm

Font styles to use
Sans Serif

Requirements
Nice to have
• It would be great to see the dynamics of a helicopter.

```html
<!DOCTYPE html>
<html lang="de">
<head>
<meta charset="utf-8">
<title>Sturmfalke Werbung – Visitenkarte</title>
<link rel="stylesheet" href="https://fonts.googleapis.com/css2?family=Oswald:wght@700&family=Saira+Condensed:wght@300;400&display=swap">
<style>
  :root {
    --card-bg: #e6e6e7;
    --brand-red: #9b2220;
    --text-dark: #3a3a3a;
  }
  * { margin: 0; padding: 0; box-sizing: border-box; }
  html, body { width: 1200px; height: 667px; overflow: hidden; background: var(--card-bg); }
  .business-card {
    position: relative;
    width: 1200px;
    height: 667px;
    background: var(--card-bg);
    font-family: "Saira Condensed", sans-serif;
    font-weight: 300;
    color: var(--text-dark);
  }
  .person {
    position: absolute;
    right: 76px;
    top: 150px;
    text-align: right;
  }
  .person-name {
    font-family: "Oswald", sans-serif;
    font-weight: 700;
    font-size: 42px;
    line-height: 60px;
    letter-spacing: -0.3px;
    color: var(--brand-red);
  }
  .person-title {
    font-size: 29px;
    line-height: 34px;
    margin-top: 2px;
  }
  .contact {
    position: absolute;
    right: 76px;
    top: 318px;
    text-align: right;
    font-size: 35px;
    line-height: 41.5px;
    font-style: normal;
  }
  .contact-numbers { margin-top: 21px; }
  .brand {
    position: absolute;
    left: 64px;
    top: 462px;
  }
  .brand-square {
    display: block;
    width: 28px;
    height: 28px;
    background: var(--brand-red);
    margin-bottom: 18px;
  }
  .brand-name {
    font-family: "Oswald", sans-serif;
    font-weight: 700;
    font-size: 26px;
    line-height: 28px;
    color: var(--text-dark);
    letter-spacing: 0.5px;
  }
  .brand-slogan {
    font-size: 17px;
    font-weight: 400;
    line-height: 20px;
    margin-top: 6px;
    color: var(--text-dark);
  }
</style>
</head>
<body>
  <main class="business-card">
    <section class="person">
      <h1 class="person-name">Rüdiger Pfannholz</h1>
      <p class="person-title">Geschäftsführer | CEO</p>
    </section>

    <address class="contact">
      <div class="contact-address">
        <p>Sturmfalke Werbung GmbH,</p>
        <p>Lindenweg 23,</p>
        <p>72619 Rebenfeld, Germany</p>
      </div>
      <div class="contact-numbers">
        <p>Phone: +49 (0) 7284 562 71 48</p>
        <p>Fax: +49 (0) 7284 562 71 77</p>
        <p>e-mail:info@sturmfalke-werbung-beispiel.de</p>
      </div>
    </address>

    <div class="brand">
      <span class="brand-square" aria-hidden="true"></span>
      <p class="brand-name">STURMFALKE<br>WERBUNG</p>
      <p class="brand-slogan">Higher Ground Web Promotion</p>
    </div>
  </main>
</body>
</html>
```